Veltrova Professional Services Website

Small website for company presence and information. Company is an IT/Telecom services company. We provide presales and installation services. Included are various company logos including color levels. Site doesn't have to use these exact colors in the logos, but should be complimentary if using different colors. It should have a professional business appearance.
Updates

My apologies for not being more responsive on the designs that have been submitted. I will be narrowing down the submissions and providing additional feedback next week. Thank you for your patience.

Project Deadline Extended
Reason: Sorry again for delays on picking designs. Work has me very busy and I've just not had the time to devote to this project. I am extending the design deadline for a few more days to give me time to make my final decisions. Thank you all for your patience. Stay tuned....

Target Market(s)

Telecom sales companies that sell Brintel telecom products.

Industry/Entity Type

Professional Service

Coding

Coded - Design and coding required

Number of Pages Required

5+ page

Font styles to use
Sans Serif

Colors
3276b5
0355a3
85abd2
85cae6
33a6d7
0692cd
ffffff

Requirements
Must have
• Professional design reflective of IT/Telecom business. A good reference website would be: http://www.quollanetworks.example/. Looking for something similar in function and presence.
Nice to have
• Rolling photos highlighting our services. Traditional navigation across the top of all pages.
Should not have
• No motion video, flashy presentation or overly confused interface.

```html
<!DOCTYPE html>
<html lang="en">
<head>
<meta charset="utf-8">
<title>Veltrova Professional Services</title>
<link href="https://fonts.googleapis.com/css2?family=Josefin+Sans:wght@400;600&family=PT+Sans+Narrow:wght@400;700&display=swap" rel="stylesheet">
<style>
:root{
  --stage:#e4e4e4;
  --white:#ffffff;
  --blue:#0692cd;
  --blue-mid:#33a6d7;
  --blue-deep:#0355a3;
  --blue-steel:#3276b5;
  --blue-pale:#85abd2;
  --blue-sky:#85cae6;
  --ink:#333b45;
}
*{margin:0;padding:0;box-sizing:border-box}
html,body{width:1200px;height:1200px;overflow:hidden;background:var(--stage)}
body{font-family:"Josefin Sans",sans-serif;color:var(--ink)}
.page{position:absolute;left:382px;top:0;width:436px;height:1200px;background:var(--white);overflow:hidden}
.abs{position:absolute}
.center{transform:translateX(-50%);text-align:center}
.narrow{font-family:"PT Sans Narrow",sans-serif}
h2,p{font-weight:400}

/* nav */
.nav{top:0;left:0;width:436px;height:27px;background:var(--white)}
.brand{left:6px;top:7px;display:flex;align-items:center;gap:3px}
.brand-mark{width:11px;height:11px;border-radius:50%;background:var(--blue-deep)}
.brand-name{font-weight:600;font-size:8.6px;color:var(--blue-deep);letter-spacing:.4px;line-height:1}
.brand-sub{font-size:2.6px;color:var(--blue-deep);letter-spacing:.3px;display:block;margin-top:1px}
.nav-home{left:114px;top:0;width:52px;height:27px;background:var(--blue-deep)}
.nav-link{top:10px;font-size:6px;color:var(--blue-deep);letter-spacing:.4px}
.nav-link.on{color:var(--white)}
.burger{left:400px;top:7px;width:16px}
.burger span{display:block;height:2.4px;background:var(--blue-deep);margin-bottom:2.6px}

/* hero */
.hero{left:0;top:27px;width:436px;height:191px;background:radial-gradient(ellipse at 60% 35%,#2a4fc0 0%,#122a8a 45%,#0a1656 100%)}
.headline{left:92px;top:37px;width:138px;padding:3px 4px;background:rgba(6,146,205,.55);color:var(--white);font-size:9px;letter-spacing:.4px;line-height:15px;white-space:nowrap}
.hero-arrow{top:78px;width:16px;height:34px}
.tile{top:119px;width:43px;height:44px;background:var(--blue);color:var(--white);font-size:5.2px;letter-spacing:.3px;text-align:center}
.tile svg{display:block;margin:7px auto 4px;width:20px;height:18px}
.dots{left:218px;top:220px;display:flex;gap:2.4px;transform:translateX(-50%)}
.dots i{width:5.5px;height:5.5px;border-radius:50%;border:1px solid var(--blue-steel)}
.dots i.on{background:var(--blue-steel)}

/* headings */
.h2{font-size:12px;color:var(--blue);letter-spacing:.6px;white-space:nowrap}

/* power */
.feat{width:72px}
.feat-icon{width:35px;height:35px;border-radius:50%;border:1.2px solid var(--blue);margin:0 auto;display:flex;align-items:center;justify-content:center}
.feat-icon.solid{background:var(--blue);box-shadow:0 0 0 2px #cfe9f6}
.feat-title{margin-top:7px;font-size:5.6px;color:var(--blue);letter-spacing:.4px;line-height:7px;height:14px}
.feat-text{margin-top:4px;font-size:4px;line-height:6.2px;text-align:justify;text-align-last:center;color:#444}
.btn{background:var(--blue);color:var(--white);font-size:4.4px;letter-spacing:.3px;text-align:center;border-radius:1px}
.btn-learn{top:390px;width:53px;height:15px;line-height:15px;border:1px solid var(--blue-sky)}

/* bands */
.band{left:0;width:436px}
.band-quote{top:422px;height:82px;background:linear-gradient(90deg,#163f86 0%,#2b5ba6 40%,#3a6fb8 50%,#2b5ba6 60%,#163f86 100%)}
.band-events{top:750px;height:109px;background:linear-gradient(180deg,#1d3f8a 0%,#2658a8 45%,#3b7fd0 80%,#1f4fa0 100%)}
.qicon{width:18px;height:18px}
.band-text{font-size:9.2px;color:var(--white);letter-spacing:.7px;white-space:nowrap}
.pager{display:flex;gap:5px;transform:translateX(-50%)}
.pager i{width:10px;height:10px;border-radius:50%;background:var(--white);display:flex;align-items:center;justify-content:center}
.pager i.dim{background:var(--blue-pale)}

/* filters */
.filters{left:218px;top:537px;display:flex;gap:4px;transform:translateX(-50%)}
.filters span{width:26px;height:10px;border:1px solid var(--blue);font-size:3px;color:var(--blue);text-align:center;line-height:8px}
.filters span.on{background:var(--blue);color:var(--white)}

/* gallery */
.shot{width:70px;height:69px}
.shot-cap{position:absolute;left:0;bottom:0;width:100%;height:9px;background:rgba(6,146,205,.75);color:var(--white);font-size:6px;line-height:9px;padding-left:1px}
.loadmore{left:218px;top:714px;font-size:4.4px;color:var(--blue)}

/* events */
.ev-title{font-size:9px;color:var(--white);letter-spacing:.8px;white-space:nowrap}
.ev-sub{font-size:3.8px;color:var(--white);width:60px;line-height:5px}
.ev-btn{width:42px;height:10px;border-radius:5px;font-size:4.4px;line-height:10px;text-align:center}
.ev-btn.fill{background:var(--blue-mid);color:var(--white)}
.ev-btn.line{background:var(--white);color:var(--blue)}

/* team */
.avatar{width:69px;height:69px;border-radius:50%;border:1.6px solid var(--blue-mid);padding:2px;background:var(--white)}
.avatar div{width:100%;height:100%;border-radius:50%}
.t-name{font-size:7.6px;color:var(--blue);letter-spacing:.4px;white-space:nowrap}
.t-role{font-size:5.6px;color:var(--blue-sky);letter-spacing:.5px;white-space:nowrap}
.t-bio{width:72px;font-size:4.3px;line-height:5.4px;color:var(--blue)}
.t-btn{width:70px;height:13px;line-height:13px;font-size:6px;top:1046px}
.team-arrow{top:956px;width:12px;height:22px}

/* footer */
.footer{left:0;top:1078px;width:436px;height:106px;background:var(--blue)}
.f-head{top:1088px;font-size:8.4px;color:var(--white);letter-spacing:.8px;white-space:nowrap}
.f-list{top:1112px;font-size:4.6px;line-height:8.2px;color:var(--white);list-style:none}
.map{left:222px;top:1106px;width:70px;height:68px;background:linear-gradient(135deg,#e6e4de 0%,#d8dde2 55%,#c9d6e0 100%)}
.social{width:18px;height:18px;border-radius:50%;background:var(--white);transform:translate(-50%,-50%)}
.copy{left:0;top:1184px;width:436px;height:16px;background:var(--blue-deep);color:var(--white);font-size:5.6px;letter-spacing:.4px;text-align:center;line-height:16px}
</style>
</head>
<body>
<main class="page">

  <header class="nav abs">
    <div class="brand abs">
      <span class="brand-mark"></span>
      <span class="brand-name">VELTROVA<span class="brand-sub">PROFESSIONAL SERVICES</span></span>
    </div>
    <div class="nav-home abs"></div>
    <span class="nav-link on abs center" style="left:140px">HOME</span>
    <span class="nav-link abs center" style="left:192px">SERVICES</span>
    <span class="nav-link abs center" style="left:244px">SUPPORT</span>
    <span class="nav-link abs center" style="left:296px">EVENTS</span>
    <span class="nav-link abs center" style="left:348px">ABOUT</span>
    <div class="burger abs"><span></span><span></span><span></span></div>
  </header>

  <section class="hero abs" role="img" aria-label="Network constellation of glowing connected nodes on deep blue">
    <div class="headline abs">THE COSTS OF DOING<br>NOTHING ARE VERY REAL.</div>
    <svg class="hero-arrow abs" style="left:8px" viewBox="0 0 16 34"><path d="M13 2 L3 17 L13 32" fill="none" stroke="#8fa9e0" stroke-width="3"/></svg>
    <svg class="hero-arrow abs" style="left:412px" viewBox="0 0 16 34"><path d="M3 2 L13 17 L3 32" fill="none" stroke="#8fa9e0" stroke-width="3"/></svg>

    <div class="tile abs" style="left:93px">
      <svg viewBox="0 0 20 18"><path d="M10 1 L1 9 H4 V17 H8 V12 H12 V17 H16 V9 H19 Z" fill="#fff"/></svg>HOME</div>
    <div class="tile abs" style="left:145px">
      <svg viewBox="0 0 20 18"><circle cx="8" cy="10" r="5" fill="none" stroke="#fff" stroke-width="2.6" stroke-dasharray="2 1.6"/><circle cx="8" cy="10" r="1.6" fill="#fff"/><circle cx="15" cy="5" r="3" fill="none" stroke="#fff" stroke-width="1.8" stroke-dasharray="1.5 1.2"/></svg>SERVICES</div>
    <div class="tile abs" style="left:196px">
      <svg viewBox="0 0 20 18"><path d="M1 9 Q10 -2 19 9 Z" fill="#fff"/><path d="M10 9 V15 Q10 17 8 17 Q6 17 6 15" fill="none" stroke="#fff" stroke-width="1.4"/></svg>SUPPORT</div>
    <div class="tile abs" style="left:248px">
      <svg viewBox="0 0 20 18"><rect x="3" y="3" width="14" height="14" fill="none" stroke="#fff" stroke-width="1.6"/><rect x="3" y="3" width="14" height="3" fill="#fff"/><g fill="#fff"><rect x="5.5" y="8" width="2" height="2"/><rect x="9" y="8" width="2" height="2"/><rect x="12.5" y="8" width="2" height="2"/><rect x="5.5" y="12" width="2" height="2"/><rect x="9" y="12" width="2" height="2"/><rect x="12.5" y="12" width="2" height="2"/></g></svg>EVENTS</div>
    <div class="tile abs" style="left:300px">
      <svg viewBox="0 0 20 18"><g fill="#fff"><circle cx="10" cy="5" r="3.2"/><circle cx="4.5" cy="7" r="2.4"/><circle cx="15.5" cy="7" r="2.4"/><path d="M4 17 Q4 9.5 10 9.5 Q16 9.5 16 17 Z"/><path d="M0 16 Q0 10 4.5 10 Q6 10 6.5 11 Q4 13 4 16 Z"/><path d="M20 16 Q20 10 15.5 10 Q14 10 13.5 11 Q16 13 16 16 Z"/></g></svg>ABOUT</div>
  </section>
  <div class="dots abs"><i></i><i></i><i class="on"></i><i></i><i></i></div>

  <h2 class="h2 abs center" style="left:218px;top:243px">THE POWER OF VELTROVA</h2>

  <div class="feat abs center" style="left:102px;top:266px">
    <div class="feat-icon solid"><svg width="18" height="18" viewBox="0 0 18 18"><g fill="none" stroke="#fff" stroke-width="1.2"><rect x="2" y="1.5" width="14" height="15"/><line x1="2" y1="5" x2="16" y2="5"/><line x1="2" y1="8.5" x2="16" y2="8.5"/><line x1="2" y1="12" x2="16" y2="12"/></g></svg></div>
    <div class="feat-title">DATA CENTER<br>SOLUTIONS</div>
    <p class="feat-text narrow">It's the brain, the place where the most critical systems are run. Data management, application performance, lifecycle management and compliance all stem from the data center, ensuring proper architecture design and limitless scalability.</p>
  </div>
  <div class="feat abs center" style="left:179px;top:266px">
    <div class="feat-icon"><svg width="20" height="18" viewBox="0 0 20 18"><g fill="none" stroke="#0692cd" stroke-width="1"><rect x="2" y="9" width="7" height="6"/><rect x="11" y="2" width="6" height="5"/><rect x="12" y="10" width="6" height="5"/><path d="M5 9 V5 H11"/><path d="M14 7 V10"/></g></svg></div>
    <div class="feat-title">UNIFIED WORKSPACE</div>
    <p class="feat-text narrow">Communication, collaboration and the take your phone everywhere mindset are driving the need to integrate voice, video, data and mobile applications, creating the linkage between the borderless user and the secure enterprise.</p>
  </div>
  <div class="feat abs center" style="left:257px;top:266px">
    <div class="feat-icon"><svg width="20" height="18" viewBox="0 0 20 18"><path d="M4 11 Q1 11 1.5 8 Q2 5.5 5 6 Q6 2 10 2.5 Q14 2.5 14.5 6 Q18.5 6 18.5 9 Q18.5 11 16 11 Z" fill="#0692cd"/><g stroke="#0692cd" stroke-width=".9"><line x1="7" y1="11" x2="7" y2="15"/><line x1="10" y1="11" x2="10" y2="16"/><line x1="13" y1="11" x2="13" y2="15"/></g></svg></div>
    <div class="feat-title">CLOUD SERVICES</div>
    <p class="feat-text narrow">What was business like before cloud? Energy consumption was rising, acquisition cycles were getting longer and resources like servers were often over-provisioned. Now is the time to talk about cloud and the many ways it can be consumed.</p>
  </div>
  <div class="feat abs center" style="left:334px;top:266px">
    <div class="feat-icon"><svg width="18" height="18" viewBox="0 0 18 18"><path d="M5.5 8 V5.5 Q5.5 2 9 2 Q12.5 2 12.5 5.5 V8" fill="none" stroke="#0692cd" stroke-width="1.6"/><rect x="3.5" y="8" width="11" height="8.5" rx="1" fill="#0692cd"/><circle cx="9" cy="12" r="1.3" fill="#fff"/></svg></div>
    <div class="feat-title">SECURITY &amp; RISK<br>MANAGEMENT</div>
    <p class="feat-text narrow">Identity and access management, malware protection and compliance. Organizations are incorporating security and risk management into every level of business planning, creating a security policy that protects the organization while enabling growth and agility.</p>
  </div>
  <a class="btn btn-learn abs center" style="left:102px">LEARN MORE</a>
  <a class="btn btn-learn abs center" style="left:179px">LEARN MORE</a>
  <a class="btn btn-learn abs center" style="left:257px">LEARN MORE</a>
  <a class="btn btn-learn abs center" style="left:334px">LEARN MORE</a>

  <section class="band band-quote abs" role="img" aria-label="Server room corridor in blue light">
    <svg class="qicon abs center" style="left:218px;top:10px" viewBox="0 0 18 18"><circle cx="9" cy="9" r="8" fill="none" stroke="#fff" stroke-width="1.3"/><text x="9" y="13" font-size="10" font-weight="700" fill="#fff" text-anchor="middle" font-family="Georgia,serif">&#8221;</text></svg>
    <p class="band-text abs center" style="left:218px;top:40px">WE REALIZE AND ACTUALIZE YOUR VISION</p>
    <div class="pager abs" style="left:218px;top:62px">
      <i class="dim"><svg width="5" height="6" viewBox="0 0 5 6"><path d="M4 .5 L1 3 L4 5.5" fill="none" stroke="#0355a3" stroke-width="1.2"/></svg></i>
      <i><svg width="5" height="6" viewBox="0 0 5 6"><path d="M1 .5 L4 3 L1 5.5" fill="none" stroke="#0355a3" stroke-width="1.2"/></svg></i>
    </div>
  </section>

  <h2 class="h2 abs center" style="left:218px;top:512px">OUR SERVICES</h2>
  <div class="filters abs narrow"><span class="on">All Projects</span><span>Services</span><span>Management</span><span>Support</span></div>

  <div class="shot abs narrow" style="left:66px;top:559px;background:linear-gradient(160deg,#9fd4ee,#5eb4df)" role="img" aria-label="Keyboard close-up with search symbol"><svg class="abs" style="left:29px;top:29px" width="12" height="12" viewBox="0 0 12 12"><circle cx="5" cy="5" r="3.6" fill="none" stroke="#fff" stroke-width="1.2"/><line x1="7.6" y1="7.6" x2="11" y2="11" stroke="#fff" stroke-width="1.3"/></svg><span class="shot-cap">Support</span></div>
  <div class="shot abs narrow" style="left:144px;top:559px;background:linear-gradient(160deg,#1b2f9a,#0b1560 60%,#2448c8)" role="img" aria-label="Engineer working in server room"><span class="shot-cap">IT/Services</span></div>
  <div class="shot abs narrow" style="left:222px;top:559px;background:radial-gradient(circle at 55% 40%,#6fb7ec,#2f6aa8 45%,#9aa7b4 100%)" role="img" aria-label="Hand holding a glowing globe"><span class="shot-cap">Management</span></div>
  <div class="shot abs narrow" style="left:299px;top:559px;background:radial-gradient(circle at 55% 45%,#e2a12c,#6a4a2a 40%,#132048 100%)" role="img" aria-label="Circuit board close-up"><span class="shot-cap">IT</span></div>
  <div class="shot abs narrow" style="left:66px;top:638px;background:linear-gradient(180deg,#dff1fb,#f4f7fa 50%,#c9d4de)" role="img" aria-label="Cloud connected to computer devices"><span class="shot-cap">Services</span></div>
  <div class="shot abs narrow" style="left:144px;top:638px;background:linear-gradient(90deg,#12236e,#3b4fb0 50%,#12236e)" role="img" aria-label="Data center aisle"><span class="shot-cap">Support</span></div>
  <div class="shot abs narrow" style="left:222px;top:638px;background:linear-gradient(90deg,#1a2e5a,#5b7aa8 50%,#1a2e5a)" role="img" aria-label="Server racks in perspective"><span class="shot-cap">Support</span></div>
  <div class="shot abs narrow" style="left:299px;top:638px;background:radial-gradient(circle at 50% 60%,#3aa0ff,#1a3b9a 45%,#0a1242)" role="img" aria-label="Illuminated circuit traces"><span class="shot-cap">IT/Support</span></div>

  <span class="loadmore abs center narrow">Load More</span>
  <svg class="abs" style="left:209px;top:723px" width="18" height="18" viewBox="0 0 18 18"><circle cx="9" cy="9" r="9" fill="#0692cd"/><path d="M5 7 L9 11 L13 7" fill="none" stroke="#fff" stroke-width="1.8"/></svg>

  <section class="band band-events abs" role="img" aria-label="Network cables plugged into a switch panel">
    <svg class="qicon abs center" style="left:218px;top:10px" viewBox="0 0 18 18"><circle cx="9" cy="9" r="8" fill="none" stroke="#fff" stroke-width="1.3"/><text x="9" y="13" font-size="10" font-weight="700" fill="#fff" text-anchor="middle" font-family="Georgia,serif">&#8221;</text></svg>

    <p class="ev-title abs center" style="left:115px;top:39px">NEWS</p>
    <p class="ev-sub abs center narrow" style="left:115px;top:55px">Our products, our culture, our employees</p>
    <span class="ev-btn fill abs center narrow" style="left:115px;top:72px">Learn More</span>
    <div class="pager abs" style="left:115px;top:91px"><i class="dim"><svg width="5" height="6" viewBox="0 0 5 6"><path d="M4 .5 L1 3 L4 5.5" fill="none" stroke="#0355a3" stroke-width="1.2"/></svg></i><i><svg width="5" height="6" viewBox="0 0 5 6"><path d="M1 .5 L4 3 L1 5.5" fill="none" stroke="#0355a3" stroke-width="1.2"/></svg></i></div>

    <p class="ev-title abs center" style="left:218px;top:39px">EVENTS</p>
    <p class="ev-sub abs center narrow" style="left:218px;top:56px">Learn the latest technology trends</p>
    <span class="ev-btn line abs center narrow" style="left:218px;top:72px">Learn More</span>
    <div class="pager abs" style="left:218px;top:91px"><i class="dim"><svg width="5" height="6" viewBox="0 0 5 6"><path d="M4 .5 L1 3 L4 5.5" fill="none" stroke="#0355a3" stroke-width="1.2"/></svg></i><i class="dim"><svg width="5" height="6" viewBox="0 0 5 6"><path d="M1 .5 L4 3 L1 5.5" fill="none" stroke="#0355a3" stroke-width="1.2"/></svg></i></div>

    <p class="ev-title abs center" style="left:322px;top:39px">PARTNERS</p>
    <p class="ev-sub abs center narrow" style="left:322px;top:56px">Key to Solution Excellence</p>
    <span class="ev-btn line abs center narrow" style="left:322px;top:72px">Learn More</span>
    <div class="pager abs" style="left:322px;top:91px"><i class="dim"><svg width="5" height="6" viewBox="0 0 5 6"><path d="M4 .5 L1 3 L4 5.5" fill="none" stroke="#0355a3" stroke-width="1.2"/></svg></i><i class="dim"><svg width="5" height="6" viewBox="0 0 5 6"><path d="M1 .5 L4 3 L1 5.5" fill="none" stroke="#0355a3" stroke-width="1.2"/></svg></i></div>
  </section>

  <h2 class="h2 abs center" style="left:218px;top:876px">OUR SERVICES</h2>
  <svg class="team-arrow abs" style="left:34px" viewBox="0 0 12 22"><path d="M10 2 L2 11 L10 20" fill="none" stroke="#0692cd" stroke-width="2.6"/></svg>
  <svg class="team-arrow abs" style="left:390px" viewBox="0 0 12 22"><path d="M2 2 L10 11 L2 20" fill="none" stroke="#0692cd" stroke-width="2.6"/></svg>

  <div class="avatar abs center" style="left:102px;top:912px"><div role="img" aria-label="Portrait of Owen Hale at a laptop" style="background:linear-gradient(160deg,#cfd8e2,#6f86a8)"></div></div>
  <div class="avatar abs center" style="left:179px;top:912px"><div role="img" aria-label="Portrait of Liam Brooks in an office" style="background:linear-gradient(160deg,#e4e6ea,#4d6384)"></div></div>
  <div class="avatar abs center" style="left:257px;top:912px"><div role="img" aria-label="Portrait of Nina Castell" style="background:linear-gradient(160deg,#3e6fae,#c9a27e 55%,#1e2f55)"></div></div>
  <div class="avatar abs center" style="left:334px;top:912px"><div role="img" aria-label="Portrait of Evan Lowe" style="background:linear-gradient(160deg,#dfe3e8,#7c8796)"></div></div>

  <p class="t-name abs center" style="left:102px;top:986px">OWEN HALE</p>
  <p class="t-role abs center" style="left:102px;top:995px">IT/SUPPORT</p>
  <p class="t-bio abs center narrow" style="left:102px;top:1003px">I was fortunate enough to have Veltrova bring me aboard as a Community Support Associate and can now help an incredible variety of people use our amazing website and services.</p>
  <a class="btn t-btn abs center narrow" style="left:102px">Learn More</a>

  <p class="t-name abs center" style="left:179px;top:986px">LIAM BROOKS</p>
  <p class="t-role abs center" style="left:179px;top:995px">IT/ENGINEER</p>
  <p class="t-bio abs center narrow" style="left:179px;top:1003px">I was fortunate enough to have Veltrova bring me aboard as a Community Support Associate and can now help an incredible variety of people use our amazing website and services.</p>
  <a class="btn t-btn abs center narrow" style="left:179px">Learn More</a>

  <p class="t-name abs center" style="left:257px;top:986px">NINA CASTELL</p>
  <p class="t-role abs center" style="left:257px;top:995px">IT/SUPPORT</p>
  <p class="t-bio abs center narrow" style="left:257px;top:1003px">I was fortunate enough to have Veltrova bring me aboard as a Community Support Associate and can now help an incredible variety of people use our amazing website and services.</p>
  <a class="btn t-btn abs center narrow" style="left:257px">Learn More</a>

  <p class="t-name abs center" style="left:334px;top:986px">EVAN LOWE</p>
  <p class="t-role abs center" style="left:334px;top:995px">ELEKTRONIC</p>
  <p class="t-bio abs center narrow" style="left:334px;top:1003px">I was fortunate enough to have Veltrova bring me aboard as a Community Support Associate and can now help an incredible variety of people use our amazing website and services.</p>
  <a class="btn t-btn abs center narrow" style="left:334px">Learn More</a>

  <footer class="footer abs"></footer>
  <p class="f-head abs center" style="left:102px">SERVICES</p>
  <p class="f-head abs center" style="left:179px">ABOUT US</p>
  <p class="f-head abs center" style="left:257px">MAP</p>
  <p class="f-head abs center" style="left:334px">SOCIAL</p>
  <ul class="f-list abs narrow" style="left:66px"><li>IT Services</li><li>IT Support</li><li>Implementation and Integration</li><li>Managed Services</li><li>Network Operations Center</li></ul>
  <ul class="f-list abs narrow" style="left:144px"><li>About Veltrova</li><li>About Team</li><li>Events</li><li>Contact Us</li><li>News</li></ul>
  <div class="map abs" role="img" aria-label="City street map showing office location"></div>

  <span class="social abs" style="left:309px;top:1114px"></span>
  <span class="social abs" style="left:334px;top:1114px"></span>
  <span class="social abs" style="left:360px;top:1114px"></span>
  <span class="social abs" style="left:309px;top:1139px"></span>
  <span class="social abs" style="left:334px;top:1139px"></span>
  <span class="social abs" style="left:360px;top:1139px"></span>
  <span class="social abs" style="left:309px;top:1164px"></span>
  <span class="social abs" style="left:334px;top:1164px"></span>
  <span class="social abs" style="left:360px;top:1164px"></span>

  <div class="copy abs">COPYRIGHT© 2017 VELTROVA ALL RIGHT RESERVED.</div>
</main>
</body>
</html>
```